Fall NHTA Postcard Design

I own Pinegrove Tumbling Athletic Club. We offer gymnastics classes to children ages 18vmonth to 18 years. We have a competitive team, an after school program and many day camps along with added on workshops. We will be offering two work shops this fall: Spanish Gymnastics... A class taught all in Spanish. Our second work shop will be Hip Hop Gymnastics.

I need a card that lets people know we are MORE than just gymnastics. We offer active options for children after school every day of the week and we are affordable. I want the front to be bright, fun and colorful and the back to have the schedule of classes we offer. I would like the front to drive people to our website: www.nhtwa.com or e-mail: info@nhtwa.com
I would like to front to offer a "Free Trial Class" *The details will be they can try it risk free, if they sign up then they pay for it as their start date. If not, no charge. Also, our after school program, sign up for 4 days get the 5th FREE! *For those who sign up for a month at a time. I have also added pictures of the gym. They are not necessary to have on the card, but put there as an option.

Our listed Mission Statement:
NHTA is dedicated to keeping kids moving! We are focused on allowing kids of all ages to be active and to have fun doing it. We encourage our students to learn gymnastics safely, while increasing self-confidence, body awareness, coordination, and skill. Children of all ages will build strength, increase flexibility, agility, balance and mental focus, while also learning how to incorporate overall fitness into a healthy lifestyle for years to come. We want to appropriately challenge each student and help them meet personal goals, while maintaining a happy and healthy environment for all.

Requirements
Must have
• Our gym Logo which is attached as the "NHTA Letter head" file.
Our contact info: www.nhtwa.com ~ Info@nhtwa.com ~ (802) 555-0147
Our class schedule on the back.
After School Program Begins: August 26th
Classes start: September 8th
"Stars" or "Bursts" on the Front with the "Free" listed on them, with an asterisk with it for the details on the back that really let you see the FREE
Must fit for a "over-sized card" looking to do 8.52"x5.47" size card
Nice to have
• A fun background picture on the front. It could be my gym or just fun bright with a "kid" having fun on it, upside down or whatever. I do not want "cluttered".
My gym colors are Black, Red and Gold but not necessary to use that color scheme.

```html
<!DOCTYPE html>
<html lang="en">
<head>
<meta charset="utf-8">
<title>Pinegrove Tumbling Athletic Club – Fall Postcard</title>
<link rel="stylesheet" href="https://fonts.googleapis.com/css2?family=Bree+Serif&family=Open+Sans:ital,wght@0,400;0,700;0,800;1,700&display=swap">
<style>
  :root {
    --page-bg: #e2e2e2;
    --card-white: #ffffff;
    --brand-red: #c8191f;
    --brand-red-dark: #8f1014;
    --brand-blue: #1d3c9a;
    --brand-blue-light: #2f6cc8;
    --band-blue-dark: #233a8e;
    --band-blue-light: #1f77c4;
    --lime: #cfd82a;
    --text-white: #ffffff;
    --gym-floor: #3b4f9a;
    --gym-wall: #d8d4d0;
  }
  * { box-sizing: border-box; margin: 0; padding: 0; }
  html, body {
    width: 1200px; height: 1000px; overflow: hidden;
    background: var(--page-bg);
  }
  .postcard {
    position: absolute; left: 40px; top: 103px;
    width: 1118px; height: 724px;
    background: var(--card-white);
    overflow: hidden;
    box-shadow: 0 1px 4px rgba(0,0,0,.18);
  }
  .postcard__wave { position: absolute; inset: 0; }
  .club-name {
    position: absolute; left: 78px; top: 38px;
    font-family: "Open Sans", sans-serif; font-weight: 400;
    font-size: 20px; letter-spacing: 3px;
    color: var(--brand-red);
  }
  .headline { position: absolute; left: 0; top: 0; width: 1118px; height: 340px; }
  .headline text {
    font-family: "Bree Serif", serif;
    fill: url(#headline-blue);
    stroke: var(--card-white); stroke-width: 12px; stroke-linejoin: round;
    paint-order: stroke fill;
  }
  .start-date {
    position: absolute; left: 360px; top: 326px;
    font-family: "Open Sans", sans-serif; font-weight: 800;
    font-size: 33px; letter-spacing: .5px;
    color: var(--text-white);
  }
  .offer-band {
    position: absolute; left: 0; top: 397px; width: 700px; height: 217px;
    background: linear-gradient(90deg, var(--band-blue-dark) 0%, var(--band-blue-light) 45%, var(--band-blue-dark) 100%);
  }
  .free-badge { position: absolute; left: 72px; top: 360px; width: 230px; height: 210px; }
  .free-badge text {
    font-family: "Open Sans", sans-serif; font-weight: 800; font-size: 44px;
    fill: var(--text-white); stroke: #7a7f14; stroke-width: 3px; paint-order: stroke fill;
  }
  .offer-list {
    position: absolute; left: 300px; top: 412px; list-style: none;
    font-family: "Open Sans", sans-serif; font-style: italic; font-weight: 700;
    font-size: 26px; line-height: 38px; color: var(--text-white);
  }
  .offer-list li { text-indent: -14px; padding-left: 14px; }
  .offer-list sup { font-size: 13px; vertical-align: 10px; }
  .offer-footnote {
    position: absolute; left: 32px; top: 587px;
    font-family: "Open Sans", sans-serif; font-style: italic; font-weight: 700;
    font-size: 12.5px; color: var(--text-white);
  }
  .gym-photo {
    position: absolute; left: 700px; top: 397px; width: 418px; height: 217px;
    background:
      linear-gradient(180deg, var(--gym-wall) 0%, #c9c2bc 32%, var(--gym-floor) 40%, #2e4287 100%);
  }
  .contact-bar {
    position: absolute; left: 0; top: 642px; width: 1118px;
    text-align: center;
    font-family: "Open Sans", sans-serif; font-weight: 700;
    font-size: 29px; letter-spacing: 1px; color: var(--text-white);
  }
</style>
</head>
<body>
  <main class="postcard">
    <svg class="postcard__wave" width="1118" height="724" viewBox="0 0 1118 724" aria-hidden="true">
      <defs>
        <radialGradient id="red-field" cx="0.55" cy="0.55" r="0.7">
          <stop offset="0" stop-color="#d81f26"/>
          <stop offset="1" stop-color="#8f1014"/>
        </radialGradient>
      </defs>
      <path d="M0 155 C 140 215 240 255 460 250 C 700 244 880 250 1118 318 L1118 724 L0 724 Z" fill="url(#red-field)"/>
    </svg>

    <p class="club-name">PINEGROVE TUMBLING ATHLETIC CLUB</p>

    <svg class="headline" viewBox="0 0 1118 340" aria-label="Keeping Kids Moving!">
      <defs>
        <linearGradient id="headline-blue" x1="0" y1="0" x2="0" y2="1">
          <stop offset="0" stop-color="#2f6cc8"/>
          <stop offset="1" stop-color="#1a3490"/>
        </linearGradient>
      </defs>
      <text x="75" y="168" font-size="80" transform="rotate(-6 75 168) skewX(-8)">Keeping</text>
      <text x="110" y="290" font-size="140" transform="rotate(-7 110 290) skewX(-8)">Kids Moving!</text>
    </svg>

    <p class="start-date">CLASSES START ON SEPTEMBER 8TH</p>

    <section class="offer-band"></section>

    <svg class="free-badge" viewBox="0 0 230 210" aria-label="Free">
      <path d="M115 12 A95 95 0 1 0 170 186 L205 200 L188 160 A95 95 0 0 0 115 12 Z" fill="#ffffff"/>
      <circle cx="115" cy="107" r="82" fill="var(--lime)"/>
      <text x="115" y="122" text-anchor="middle" transform="rotate(-14 115 107)">FREE!</text>
    </svg>

    <ul class="offer-list">
      <li>• Free Trial Class<sup>*</sup></li>
      <li>• After school program<br>sign up for 4 days get<br>the 5th Free<sup>**</sup></li>
    </ul>
    <p class="offer-footnote">*Try it risk free, sign up and start pay that date. If not, no charge. **If sign up for amonth at a time.</p>

    <div class="gym-photo" role="img" aria-label="Photo of the gym floor with colourful mats, a bounce house and play equipment"></div>

    <p class="contact-bar">(802) 555-0147 • WWW.NHTWA.COM • INFO@NHTWA.COM</p>
  </main>
</body>
</html>
```